Makeup artist looking for business card design

- Business card to be memorable and recognisable

- I've attached photos of my logo (File 4), photos that I want to incorporate into the design (File 5,6 & 7) and an example of the design I like "Mirela Stott" (File 1)

- I've attached 3 photos of the designs I want to use, please use one of your choice

- Next to Instagram (File 2) and Facebook (File 3), please use their logo.

- No coloured background, either use the original background (grey) old white.

- Please include the following on the business card:
- Business name: LK Makeup Artistry
- My name: Rosalind Kerr
- Occupation: Makeup Artist
- Contact number: 0437 295 148
- Email: roskerr_makeup@mailvento.com
- Instagram (please use image): @lkmakeupartistry
- Facebook (please use image): www.socialnook.com/LKMakeUpArtistry

Target Market(s)

Target woman for bridal makeup, occasion, fashion makeup and print.

Industry/Entity Type

Business

Requirements
Must have
• Logo provided and photo provided
Should not have
• Colourful background
Too cluttered
Shouldn't use old style font

```html
<!DOCTYPE html>
<html lang="en">
<head>
<meta charset="utf-8">
<title>LK Makeup Artistry – Business Card</title>
<link href="https://fonts.googleapis.com/css2?family=Open+Sans:wght@300;400;700&display=swap" rel="stylesheet">
<style>
  :root {
    --page-bg: #e6e6e8;
    --card-bg: #f4f3f7;
    --ink: #1c1c1c;
    --ink-soft: #555558;
    --accent-bar: #111111;
    --photo-light: #f1e6ee;
    --photo-mid: #c98bbd;
    --photo-deep: #7d3f78;
    --photo-skin: #d7a597;
  }
  * { box-sizing: border-box; margin: 0; padding: 0; }
  html, body {
    width: 1200px; height: 1200px; overflow: hidden;
    background: var(--page-bg);
    font-family: "Open Sans", Arial, sans-serif;
    color: var(--ink);
  }
  .sheet {
    position: relative; width: 1200px; height: 1200px;
    display: flex; flex-direction: column; align-items: center; justify-content: center; gap: 60px;
  }
  .card {
    position: relative; width: 600px; height: 343px;
    background: var(--card-bg);
    box-shadow: 0 6px 20px rgba(0,0,0,0.12);
    overflow: hidden;
  }
  /* Front */
  .front__brand {
    position: absolute; left: 34px; top: 120px; width: 160px;
    font-size: 18px; font-weight: 300; letter-spacing: 0.14em; line-height: 1.5;
    color: var(--ink); text-transform: uppercase;
  }
  .front__photo {
    position: absolute; left: 190px; top: 0; right: 0; bottom: 0;
    background:
      radial-gradient(ellipse 42% 48% at 68% 62%, var(--photo-mid) 0%, var(--photo-deep) 45%, transparent 75%),
      radial-gradient(ellipse 30% 55% at 32% 42%, var(--photo-skin) 0%, transparent 70%),
      linear-gradient(180deg, var(--photo-light) 0%, #e8d2e2 60%, #d9b4cf 100%);
  }
  /* Back */
  .back__bar {
    position: absolute; left: 48px; width: 9px; background: var(--accent-bar);
  }
  .back__bar--top { top: 40px; height: 52px; }
  .back__bar--bottom { top: 222px; height: 28px; }
  .back__details { position: absolute; left: 76px; top: 70px; }
  .back__name { font-size: 20px; font-weight: 700; line-height: 1.2; }
  .back__role { font-size: 14px; font-weight: 400; color: var(--ink-soft); margin-bottom: 22px; }
  .contact-list { list-style: none; }
  .contact-list li {
    display: flex; align-items: center; gap: 12px;
    font-size: 15px; line-height: 26px; color: var(--ink);
  }
  .contact-list svg { width: 16px; height: 16px; flex: none; }
  .icon-square { width: 14px; height: 14px; background: var(--ink-soft); flex: none; margin: 0 1px; }
  .back__brand {
    position: absolute; right: 36px; top: 150px; width: 150px;
    font-size: 16px; font-weight: 300; letter-spacing: 0.14em; line-height: 1.5;
    text-transform: uppercase; color: var(--ink); text-align: left;
  }
</style>
</head>
<body>
<main class="sheet">
  <section class="card card--front">
    <p class="front__brand">LK Makeup Artistry</p>
    <div class="front__photo" role="img" aria-label="Fashion makeup portrait of a model beside a large pink-purple flower"></div>
  </section>

  <section class="card card--back">
    <span class="back__bar back__bar--top"></span>
    <span class="back__bar back__bar--bottom"></span>
    <div class="back__details">
      <h1 class="back__name">Rosalind Kerr</h1>
      <p class="back__role">Makeup Artist</p>
      <ul class="contact-list">
        <li>
          <svg viewBox="0 0 16 16" aria-hidden="true"><rect x="4" y="1" width="8" height="14" rx="1.5" fill="none" stroke="#1c1c1c" stroke-width="1.6"/><line x1="7" y1="12.5" x2="9" y2="12.5" stroke="#1c1c1c" stroke-width="1.4"/></svg>
          +0437 295 148
        </li>
        <li>
          <svg viewBox="0 0 16 16" aria-hidden="true"><rect x="1" y="3.5" width="14" height="9" fill="none" stroke="#1c1c1c" stroke-width="1.5"/><polyline points="1,3.5 8,9 15,3.5" fill="none" stroke="#1c1c1c" stroke-width="1.5"/></svg>
          roskerr_makeup@mailvento.com
        </li>
        <li><span class="icon-square"></span>@lkmakeupartistry</li>
        <li><span class="icon-square"></span>www.socialnook.com/LKMakeUpArtistry</li>
      </ul>
    </div>
    <p class="back__brand">LK Makeup Artistry</p>
  </section>
</main>
</body>
</html>
```